Blueprint and Beyond - Invitation

Need a three fold, 8.5 X 11 invitation that will be direct mail for a seminar. We develop properties for churches in the United States. Final design should communicate a compelling reason for church leaders to attend the "Blueprint and Beyond" seminar. To be clear, the folded and complete invitation is 8.5" X 11" so there are a total of 6 panels measuring 8.5" X 11". Thanks and have fun.
Updates

Went on vacation/holiday

Target Market(s)

Young start up churches, highly energetic, not traditional at all.

Colors
0054AA
0677BA
7BADD7
CADEEF
E8F1F8
FFF300
FFF600
FEFA6F
FFFEC7
FFFEE8
FFC000
F8CF3A
FAE287
FDF2CF
FEFAEE
EB3D1F
EC4F4E
F09395
F8D3D4
FCEDEE

Requirements
Must have
• See the mock up brochure that I made up. It has all the info I need.
Nice to have
• Open space. Mock up is much too busy looking. Gives me a headache!
Should not have
• Nothing traditional church looking.

```html
<!DOCTYPE html>
<html lang="en">
<head>
<meta charset="utf-8">
<title>Blueprint and Beyond – Seminar Invitation</title>
<link href="https://fonts.googleapis.com/css2?family=Montserrat:ital,wght@0,500;0,600;0,700;1,500;1,600;1,700&family=Playfair+Display:ital,wght@0,700;1,700&display=swap" rel="stylesheet">
<style>
:root{
  --blue-deep:#0054AA;
  --blue:#0677BA;
  --blue-soft:#7BADD7;
  --blue-pale:#CADEEF;
  --blue-mist:#E8F1F8;
  --yellow:#FFC000;
  --yellow-warm:#F8CF3A;
  --yellow-soft:#FAE287;
  --yellow-pale:#FDF2CF;
  --red:#EB3D1F;
  --red-soft:#EC4F4E;
  --ink:#10243d;
  --white:#ffffff;
}
*{margin:0;padding:0;box-sizing:border-box}
html,body{width:1026px;height:1200px;overflow:hidden;background:var(--white)}
body{position:relative;font-family:"Montserrat",sans-serif}
.brochure{position:absolute;left:24px;top:284px;width:978px;height:632px;display:flex;box-shadow:0 26px 30px -18px rgba(0,0,0,.4)}
.panel{position:relative;width:326px;height:632px;overflow:hidden}
.panel-left{background:var(--blue-deep)}
.panel-middle{background:var(--blue-mist)}
.panel-right{background:var(--blue-deep)}
.abs{position:absolute}
.photo{position:absolute}
/* left panel */
.intro{position:absolute;left:0;top:118px;width:326px;height:212px;background:var(--blue);text-align:center;color:var(--white)}
.intro .kicker{font-family:"Playfair Display",serif;font-style:italic;font-weight:700;font-size:17px;margin-top:28px;letter-spacing:.5px}
.intro .headline{font-family:"Playfair Display",serif;font-weight:700;font-size:16px;color:var(--yellow-soft);margin-top:2px}
.intro .lead{font-style:italic;font-weight:600;font-size:13px;line-height:23px;margin-top:6px}
.dates{position:absolute;top:330px;left:0;width:326px;height:43px;background:var(--yellow-soft);color:var(--ink);text-align:center;font-weight:700;font-size:11px;line-height:16px;padding-top:6px}
.price{position:absolute;top:376px;left:0;width:326px;height:27px;background:var(--red);color:var(--white);text-align:center;font-weight:700;font-size:10.5px;line-height:27px}
.topics-title{position:absolute;top:414px;left:0;width:326px;text-align:center;color:var(--yellow);font-weight:700;font-size:14.5px;line-height:22px;text-decoration:underline}
.topics{position:absolute;top:474px;left:8px;display:flex;gap:6px}
.topics ul{list-style:none;color:var(--white);font-style:italic;font-weight:600;font-size:9.2px;line-height:15.8px}
.topics li{padding-left:9px;position:relative}
.topics li::before{content:"";position:absolute;left:1px;top:7px;width:3px;height:3px;border-radius:50%;background:var(--white)}
.topics ul.col-a{width:160px}
.topics ul.col-b{width:146px;font-size:8.4px;line-height:14px}
/* middle panel */
.quote{position:absolute;left:26px;top:32px;width:282px;height:136px}
.quote p{position:absolute;left:18px;top:11px;width:250px;color:var(--white);font-style:italic;font-weight:600;font-size:7.7px;line-height:13px}
.portrait{position:absolute;border-radius:50%;border:3px solid var(--yellow)}
.pastors{position:absolute;left:134px;top:186px;color:var(--blue-deep);font-style:italic;font-weight:700;font-size:11px;line-height:17px}
.badnews{position:absolute;left:0;top:434px;width:326px;height:137px;background:var(--yellow-pale);padding:5px 6px;color:var(--ink);font-style:italic;font-weight:600;font-size:7.6px;line-height:12.6px}
.badnews .label{text-decoration:underline;font-weight:700;color:var(--red)}
.mailing{position:absolute;top:586px;left:0;width:326px;text-align:center;color:var(--red);font-weight:700;font-size:17px}
/* right panel */
.header{position:absolute;left:0;top:0;width:326px;height:185px;background:var(--blue-mist)}
.header-bar{position:absolute;left:0;top:0;width:326px;height:74px;background:var(--blue-deep)}
.brand{position:absolute;left:118px;top:14px;display:flex;align-items:center;gap:8px;color:var(--white);font-weight:500;letter-spacing:1px}
.brand .dot{width:22px;height:22px;border-radius:50%;background:var(--yellow);flex:none}
.brand .name{display:block;font-size:22px;line-height:24px}
.brand .tag{display:block;font-size:11px;line-height:14px;letter-spacing:1.6px}
.register{position:absolute;right:3px;top:84px;text-align:right;color:var(--ink);font-weight:700;font-size:9.2px;line-height:20px}
.register em{font-style:italic;color:var(--red)}
.developer{position:absolute;left:4px;top:122px;color:var(--blue-deep);font-weight:700;font-size:11.4px;line-height:18px}
.developer .name{font-style:italic}
.contact{position:absolute;left:184px;top:136px;color:var(--ink);font-weight:700;font-size:8.8px;line-height:14.5px}
.contact div{display:flex;align-items:center;gap:3px;white-space:nowrap}
.contact svg{width:10px;height:10px;flex:none}
.help{position:absolute;left:0;top:420px;width:326px;height:64px;text-align:center;color:var(--white);font-weight:700;font-size:15.5px;line-height:23px;padding-top:6px}
.benefits{position:absolute;left:10px;top:500px;width:310px;list-style:none;color:var(--white);font-style:italic;font-weight:600;font-size:9.2px;line-height:16.2px}
.benefits li{padding-left:10px;position:relative}
.benefits li::before{content:"";position:absolute;left:1px;top:7px;width:3px;height:3px;border-radius:50%;background:var(--yellow)}
.footer-edge{position:absolute;left:0;bottom:0;width:978px;height:8px;background:var(--yellow)}
</style>
</head>
<body>
<main class="brochure">
  <section class="panel panel-left">
    <div class="photo" role="img" aria-label="Photo of a modern church building with lawn and walkway" style="left:0;top:0;width:326px;height:124px;background:linear-gradient(180deg,#bcd6ea 0%,#e8e2d2 55%,#7fae52 85%,#5f8f3e 100%)"></div>
    <div class="intro">
      <svg class="abs" style="left:0;top:-14px" width="326" height="20" viewBox="0 0 326 20" preserveAspectRatio="none"><path d="M0 14 L20 8 L38 13 L60 6 L84 12 L110 7 L136 13 L160 6 L186 12 L212 7 L238 13 L262 6 L290 12 L310 8 L326 12 L326 20 L0 20Z" fill="#0677BA"/><path d="M0 14 L20 8 L38 13 L60 6 L84 12 L110 7 L136 13 L160 6 L186 12 L212 7 L238 13 L262 6 L290 12 L310 8 L326 12" stroke="#fff" stroke-width="2" fill="none"/></svg>
      <div class="kicker">PASTOR!</div>
      <div class="headline">Lead your church with confidence.</div>
      <div class="lead">Attend the Blueprint and Beyond Seminar<br>Learn how to<br>DESIGN, FINANCE, and BUILD<br>the most creative, functional, and<br>affordable church facilities in America!</div>
    </div>
    <div class="dates">Coming to the Bay Area, March 4–7<br>Santa Rosa | Walnut Creek | San Jose | San Mateo</div>
    <div class="price">SEMINAR COST IS JUST $29 AND INCLUDES LUNCH!</div>
    <div class="topics-title">THE SEMINAR TEACHES A VARIETY OF<br>TOPICS INCLUDING:</div>
    <div class="topics">
      <ul class="col-a">
        <li>10-Steps to Your New Facility</li>
        <li>Creative Land Acquisition</li>
        <li>Funding Your Building Program</li>
        <li>What Type of Building is Right for You</li>
        <li>Creative Church Designs</li>
        <li>Time and Talent Surveys</li>
      </ul>
      <ul class="col-b">
        <li>Meet Your Development Team</li>
        <li>Debt-Free Development</li>
        <li>Understanding the Permit Process</li>
        <li>Dealing with Nasty Neighbors</li>
        <li>Developing a Communication Plan</li>
        <li>Master Planning Your Campus</li>
      </ul>
    </div>
  </section>

  <section class="panel panel-middle">
    <svg class="quote" viewBox="0 0 282 136" aria-hidden="true"><path d="M18 6 C80 -4 200 2 258 8 C290 14 284 60 276 96 C270 130 230 132 180 130 C120 128 40 134 16 124 C-6 110 2 60 4 30 C6 12 10 8 18 6Z" fill="#7BADD7" transform="translate(6,4)"/><path d="M18 6 C80 -4 200 2 258 8 C284 14 280 60 272 96 C266 126 230 128 180 126 C120 124 40 130 16 120 C-4 108 2 60 4 30 C6 12 10 8 18 6Z" fill="#0677BA"/></svg>
    <div class="quote"><p>“I remember sitting at my desk back in 2001, wondering what am I going to do? Wishing that there was someone I could call that had the knowledge and experience to guide me in the right direction. That is when a seminar invitation showed up on my desk, and I soon met Dan Whitcombe. Since then, Cedar Hill Fellowship has gone through numerous building programs, grown to over 5,000 in attendance, and grown into a thriving ministry with a high global impact.”</p></div>
    <div class="portrait" role="img" aria-label="Portrait photo of the pastor couple" style="left:10px;top:166px;width:110px;height:110px;background:radial-gradient(circle,#c9a68c,#7a5a44)"></div>
    <div class="pastors">PASTOR MARK &amp; LENA<br>HARTLEY<br>CEDAR HILL FELLOWSHIP<br>MAPLE GROVE, TEXAS</div>
    <svg class="abs" style="left:0;top:262px" width="326" height="170" viewBox="0 0 326 170" role="img" aria-label="Photo of a modern church campus with glass entrance">
      <defs><linearGradient id="campus" x1="0" y1="0" x2="0" y2="1"><stop offset="0" stop-color="#c7dff0"/><stop offset=".55" stop-color="#d9d6cc"/><stop offset=".8" stop-color="#8f8a80"/><stop offset="1" stop-color="#7aa04a"/></linearGradient></defs>
      <path d="M138 10 C180 -4 250 4 290 24 C318 40 310 100 300 126 C286 160 200 166 140 160 C80 156 20 162 6 130 C-4 104 8 60 40 50 C80 40 100 24 138 10Z" fill="url(#campus)"/>
    </svg>
    <div class="badnews"><span class="label">Here's the bad news:</span><br>The average tenure of a pastor after a significant building project is twenty-two months. Over half of the churches in the U.S. have a set of plans (stuck behind the pastor's door) that will never be built. To top it off, construction is the second most litigated industry in the U.S., behind medical.<br>Some pastors will deal with these statistics by never building. Some will forge ahead alone and often become one of these statistics. The good news is that others will seek out those who have built to gain counsel and wisdom.<br>“Plans fail for lack of counsel, but with many advisors they succeed.”<br>– Proverbs 15:22</div>
    <div class="mailing">MAILING INFO GOES HERE</div>
  </section>

  <section class="panel panel-right">
    <div class="header">
      <div class="header-bar"></div>
      <div class="portrait" role="img" aria-label="Portrait photo of the church developer" style="left:-2px;top:4px;width:98px;height:98px;background:radial-gradient(circle,#c9a48a,#5c4a3a)"></div>
      <div class="brand"><span class="dot"></span><span><span class="name">WHITCOMBE</span><span class="tag">facility solutions</span></span></div>
      <div class="register">[CONTACT DAN WHITCOMBE TO REGISTER]<br><em>SEATING IS LIMITED</em></div>
      <div class="developer"><span class="name">DANIEL R. WHITCOMBE</span><br>AMERICA'S #1<br>CHURCH DEVELOPER</div>
      <div class="contact">
        <div><svg viewBox="0 0 10 10"><circle cx="5" cy="5" r="4.2" fill="none" stroke="#10243d" stroke-width="1"/><path d="M1 5h8M5 1c-2 2.5-2 5.5 0 8M5 1c2 2.5 2 5.5 0 8" fill="none" stroke="#10243d" stroke-width=".8"/></svg>Danwhitcombe.com</div>
        <div><svg viewBox="0 0 10 10"><circle cx="5" cy="5" r="4.2" fill="none" stroke="#10243d" stroke-width="1"/><rect x="2.6" y="3.3" width="4.8" height="3.4" fill="none" stroke="#10243d" stroke-width=".8"/><path d="M2.6 3.3L5 5.2L7.4 3.3" fill="none" stroke="#10243d" stroke-width=".8"/></svg>dan@whitcombe.org</div>
        <div><svg viewBox="0 0 10 10"><circle cx="5" cy="5" r="4.8" fill="#10243d"/><path d="M3.4 2.6l1 1-.6.8c.4.8 1 1.4 1.8 1.8l.8-.6 1 1-.8.9c-1.8-.3-3.7-2.2-4-4z" fill="#fff"/></svg>555-210-4871</div>
      </div>
    </div>
    <div class="photo" role="img" aria-label="Photo of a seminar audience watching a presenter and a projected site plan" style="left:0;top:185px;width:326px;height:297px;background:linear-gradient(180deg,#3c4452 0%,#2f6a58 25%,#3a3a40 45%,#6d5a4c 75%,#8a7464 100%)"></div>
    <svg class="abs" style="left:0;top:418px" width="326" height="64" viewBox="0 0 326 64" aria-hidden="true"><path d="M6 10 C60 2 150 6 230 4 C280 2 312 8 324 12 L320 58 C260 62 180 56 110 60 C60 62 20 58 0 54 L10 34Z" fill="#EB3D1F"/></svg>
    <div class="help">WE HELP PASTORS AND<br>CHURCH LEADERS TO</div>
    <ul class="benefits">
      <li>Develop state-of-the-art facilities that are functional &amp; affordable</li>
      <li>Reduce the stress and distractions of a building program</li>
      <li>Avoid the pitfalls of typical building projects</li>
      <li>Eliminate those unexpected surprises</li>
      <li>Maximize Ministry Momentum by eliminating growth barriers</li>
    </ul>
  </section>
  <div class="footer-edge"></div>
</main>
</body>
</html>
```